Business Card Design

We need a business card designed for our new company. Prefer a black card with white logo & writing.

Contact Information for Business Card

Dale Pickett, address: 7-4417 Larchmere Avenue, Abbotsford, BC, V3K 2R9, Office Phone: 604-555-0172, Cell: 604-555-0138, Email: dale@kelsoncoatworks.ca

Colors

Designer to choose only greyscale colors for use in the design.

```html
<!DOCTYPE html>
<html lang="en">
<head>
<meta charset="utf-8">
<title>Kelson Coatworks — Business Card</title>
<link href="https://fonts.googleapis.com/css2?family=Montserrat:wght@700;800&family=Lato:wght@300;400&display=swap" rel="stylesheet">
<style>
  :root {
    --page: #2f2f2f;
    --card: #222223;
    --ink: #ffffff;
    --ink-soft: #d9d9d9;
    --rule: #8a8a8a;
  }
  * { margin: 0; padding: 0; box-sizing: border-box; }
  html, body {
    width: 1200px; height: 895px; overflow: hidden;
    background: var(--page);
  }
  .canvas { position: relative; width: 1200px; height: 895px; }
  .card {
    position: absolute;
    width: 560px; height: 320px;
    background: var(--card);
    border-radius: 22px;
    box-shadow: 0 18px 40px rgba(0,0,0,0.45);
    color: var(--ink);
  }
  .card--front { left: 110px; top: 95px; }
  .card--back  { left: 530px; top: 480px; }

  .brand-name {
    position: absolute;
    font-family: "Montserrat", sans-serif;
    font-weight: 800;
    color: var(--ink);
    text-transform: uppercase;
    line-height: 1.05;
    letter-spacing: 0.02em;
    text-align: center;
  }
  .card--front .brand-name {
    left: 0; right: 0; top: 112px;
    font-size: 40px;
  }
  .card--back .brand-name {
    left: 30px; width: 250px; top: 176px;
    font-size: 27px;
  }

  .divider {
    position: absolute;
    left: 300px; top: 40px;
    width: 1px; height: 240px;
    background: linear-gradient(to bottom, transparent, var(--rule) 20%, var(--ink) 55%, transparent);
  }
  .contact {
    position: absolute;
    left: 328px; top: 46px;
    font-family: "Lato", sans-serif;
    font-size: 16px;
    color: var(--ink);
  }
  .contact__name {
    font-family: "Montserrat", sans-serif;
    font-weight: 700;
    font-size: 21px;
  }
  .contact__title {
    font-weight: 300;
    font-size: 17px;
    color: var(--ink-soft);
    margin-bottom: 10px;
  }
  .contact__list { list-style: none; }
  .contact__item {
    display: flex; align-items: center; gap: 10px;
    height: 26px;
  }
  .contact__icon { width: 15px; height: 15px; flex: none; }
  .contact__address { margin-top: 16px; line-height: 1.45; }
</style>
</head>
<body>
<main class="canvas">
  <section class="card card--front" aria-label="Card front">
    <div class="brand-name">Kelson<br>Coatworks</div>
  </section>

  <section class="card card--back" aria-label="Card back">
    <div class="brand-name">Kelson<br>Coatworks</div>
    <div class="divider"></div>
    <div class="contact">
      <div class="contact__name">Dale Pickett</div>
      <div class="contact__title">President</div>
      <ul class="contact__list">
        <li class="contact__item">
          <svg class="contact__icon" viewBox="0 0 24 24" fill="#fff"><path d="M6.6 10.8a15 15 0 0 0 6.6 6.6l2.2-2.2a1 1 0 0 1 1-.25 11.4 11.4 0 0 0 3.6.57 1 1 0 0 1 1 1V20a1 1 0 0 1-1 1A17 17 0 0 1 3 4a1 1 0 0 1 1-1h3.5a1 1 0 0 1 1 1c0 1.25.2 2.45.57 3.57a1 1 0 0 1-.25 1z"/></svg>
          604-555-0172
        </li>
        <li class="contact__item">
          <svg class="contact__icon" viewBox="0 0 24 24" fill="none" stroke="#fff" stroke-width="2"><rect x="6" y="2" width="12" height="20" rx="2"/><line x1="11" y1="18" x2="13" y2="18"/></svg>
          604-555-0138
        </li>
        <li class="contact__item">
          <svg class="contact__icon" viewBox="0 0 24 24" fill="none" stroke="#fff" stroke-width="2"><rect x="2" y="5" width="20" height="14"/><polyline points="2,5 12,13 22,5"/></svg>
          dale@kelsoncoatworks.ca
        </li>
      </ul>
      <div class="contact__address">7-4417 Larchmere Avenue,<br>Abbotsford, BC, V3K 2R9,</div>
    </div>
  </section>
</main>
</body>
</html>
```